Website For Ladder Company

I have a client that needs a new look to a stale website. Notes:

They like the the grays and reds of trelvaquip.com

i like the layout of this theme so i can get them a responsive design but it is a little too clean / white and needs some more color. I like this font and typography style http://fennimarklabs.com/

They like the layout of vurx.com but not black

Current site is halbrenner.com but I want to make sure you work directly through me and NOT CONTACT THE CLIENT DIRECTLY

There needs to be a blog feed section, place for featured video, intro paragraph and get all their current navigation.

there will be no flash on the site but a similar way they have the different types of ladder categories should be integrated

I envisioned this image in the header in some fashion http://www.plivorabank.com/cat.mhtml?searchterm=on+a+ladder&search_group=&lang=en&search_source=search_form#id=274519036&src=93k_4TRmpaQ8LdeYwnBzKv-7-41 with a tagline over it saying

Now Would Be a Good Time to Know What Ladder You Use. Trust Halbrenner.

Industry/Entity Type

Fashion

```html
<!DOCTYPE html>
<html lang="en">
<head>
<meta charset="utf-8">
<title>Halbrenner Ladders</title>
<link href="https://fonts.googleapis.com/css2?family=Signika:wght@300;400;600&family=Open+Sans:wght@300;400&display=swap" rel="stylesheet">
<style>
:root{
  --red:#d0101c;
  --red-dark:#a90d14;
  --ink:#333;
  --muted:#6b6b6b;
  --line:#d9d9d9;
  --footer:#f0f0f0;
  --caption:rgba(20,20,20,.85);
  --ladder-orange:#f3c7a3;
  --ladder-chrome:#dcdcdc;
}
*{margin:0;padding:0;box-sizing:border-box}
html,body{width:1138px;height:1200px;overflow:hidden;background:#fff}
body{position:relative;font-family:"Open Sans",sans-serif;color:var(--ink)}
.topbar{position:absolute;left:0;top:0;width:1138px;height:6px;background:#e6e6e6}
.utility{position:absolute;right:78px;top:17px;font-size:13px;color:var(--muted);font-weight:300}
.utility span{margin:0 6px}
.brand{position:absolute;left:60px;top:36px;font-family:"Signika",sans-serif;font-weight:600;font-size:52px;color:var(--red);letter-spacing:-1px}
.nav{position:absolute;right:51px;top:68px;display:flex;font-family:"Signika",sans-serif;font-weight:400;font-size:19px;color:#444}
.nav a{padding:8px 17px 15px;border-left:1px solid #e3e3e3;color:inherit;text-decoration:none}
.nav a:first-child{border-left:none}
.hero{position:absolute;left:54px;top:116px;width:1024px;height:391px;background:linear-gradient(110deg,#dcdcd8 0%,#bfc5c6 30%,#5aa0e6 55%,#7db8f0 100%)}
.caption{position:absolute;left:54px;top:328px;width:422px;height:128px;background:var(--caption);clip-path:polygon(0 0,100% 0,94% 100%,0 100%);color:#fff;font-family:"Signika",sans-serif;padding:16px 25px}
.caption h1{font-weight:300;font-size:28px;line-height:1.2}
.caption h2{font-weight:400;font-size:21px;line-height:1.3}
.caption p{font-family:"Open Sans",sans-serif;font-weight:300;font-size:14px;color:#ccc;margin-top:6px}
.pager{position:absolute;left:1036px;top:474px;width:42px;height:33px;background:rgba(255,255,255,.85)}
.card{position:absolute;border:1px solid var(--line);background:#fff}
.launch{left:54px;top:525px;width:422px;height:278px}
.launch .img{position:absolute;left:10px;top:8px;width:400px;height:212px;background:linear-gradient(90deg,#fff 0%,var(--ladder-orange) 25%,#fff 50%,var(--ladder-chrome) 75%,#fff 100%)}
.launch .band{position:absolute;left:0;bottom:0;width:420px;height:52px;background:linear-gradient(#e21017,var(--red-dark));color:#fff;font-family:"Signika",sans-serif;font-weight:600;font-size:19px;padding:14px 24px}
.tile{position:absolute;top:525px;width:280px;height:204px}
.tile .band{position:absolute;left:0;bottom:0;width:100%;height:50px;background:rgba(215,215,215,.9);font-family:"Signika",sans-serif;font-weight:400;font-size:19px;color:#555;padding:15px 20px}
.tile.why{left:501px;background:linear-gradient(#8e4a3e,#b86c5c 60%,#e7dfd2)}
.tile.feature{left:797px;background:linear-gradient(120deg,#e8e8e4,#cfd0c9 60%,#b7b8b0)}
h3.section{font-family:"Signika",sans-serif;font-weight:400;color:var(--red);font-size:21px}
.services{left:54px;top:814px;width:422px;height:217px;background:linear-gradient(#fff 60%,#eee)}
.services h3{position:absolute;left:25px;top:16px}
.services .img{position:absolute;left:18px;top:44px;width:128px;height:118px;background:linear-gradient(#d8d8d8,#8a8f96)}
.services .body{position:absolute;left:160px;top:52px;width:250px}
.services h4{font-weight:300;font-size:16px;color:#444;margin-bottom:6px}
.services p{font-size:12.5px;font-weight:300;color:var(--muted);line-height:20px}
.btn{display:inline-block;margin-top:10px;background:linear-gradient(#e21017,var(--red-dark));color:#fff;font-size:10px;padding:7px 13px;border-radius:2px}
.latest{left:501px;top:747px;width:578px;height:284px;padding:18px 22px 18px 24px}
.latest h3{margin-bottom:12px}
.latest h4{font-weight:400;font-size:14px;color:#333;margin-bottom:5px}
.latest p{font-size:12.6px;font-weight:300;color:var(--muted);line-height:20px;margin-bottom:18px;letter-spacing:-.1px}
.footer{position:absolute;left:0;top:1078px;width:1138px;height:122px;background:var(--footer);border-top:1px solid #e2e2e2}
.footer .links{position:absolute;left:52px;top:24px;font-size:14px;color:#555;font-weight:300}
.footer .links span{margin:0 9px}
.footer .copy{position:absolute;left:52px;top:60px;font-size:13px;color:#777;font-weight:300}
.footer svg{position:absolute;left:932px;top:22px}
</style>
</head>
<body>
<div class="topbar"></div>
<div class="utility">Options<span>|</span>Trade Shows<span>|</span>Sitemap<span>|</span>Liberay<span>|</span>FAQ</div>
<div class="brand">Halbrenner</div>
<nav class="nav"><a>Home</a><a>Features</a><a>What's New</a><a>Products</a><a>Replacement Parts</a><a>Contact</a></nav>

<div class="hero" role="img" aria-label="Man in white shirt climbing an aluminium ladder against a house roof under blue sky"></div>
<div class="caption">
  <h1>Now Would Be a Good Time to</h1>
  <h2>Know What Ladder You Use.</h2>
  <p>Trust Halbrenner</p>
</div>
<div class="pager"><svg width="42" height="33"><path d="M16 10l-5 6.5 5 6.5M26 10l5 6.5-5 6.5" fill="none" stroke="#333" stroke-width="2"/></svg></div>

<div class="card launch">
  <div class="img" role="img" aria-label="Orange rolling warehouse ladder with a worker carrying a box, beside a chrome rolling step ladder"></div>
  <div class="band">LATEST PRODUCTS LAUNCHED</div>
</div>
<div class="tile why" role="img" aria-label="Worker on ladder repairing a house gutter"><div class="band">WHY CHOOSE US</div></div>
<div class="tile feature" role="img" aria-label="Smiling worker in hard hat and safety vest"><div class="band">FEATURE SERVICES</div></div>

<div class="card services">
  <h3 class="section">Customer Services &amp; Products</h3>
  <div class="img" role="img" aria-label="Two business people wearing hard hats"></div>
  <div class="body">
    <h4>Nunc tempus felis vitae</h4>
    <p>Morbi ornare gravida elit. Integer congue, augue et malesuada iaculis, ipsum dui aliquet felis, at cursus magna nisl nec elit. Donec iaculis diam a nisi accumsan viverra</p>
    <span class="btn">READ MORE</span>
  </div>
</div>

<div class="card latest">
  <h3 class="section">Latest Products</h3>
  <h4>Duis tincidunt lectus quis</h4>
  <p>Donec scelerisque leo ac risus. Praesent sit amet est. In dictum, dolor eu dictum porttitor</p>
  <h4>Suspendisse quam leo</h4>
  <p>Nunc tempus felis vitae urna. Vivamus porttitor, g, purus nisi eleifend libero, a tempus libero lectus feugiat felis. Morbi diam mauris, viverra in, gravida eu, mattis in, ante.</p>
  <h4>Lorem ipsum dolor sit amet</h4>
  <p>Morbi ut mi. Nullam enim leo, egestas id, condimentum at, laoreet mattis, massa.</p>
</div>

<footer class="footer">
  <div class="links">Home<span>/</span>Features<span>/</span>What's New<span>/</span>Products<span>/</span>Replacement Parts<span>/</span>Contact</div>
  <div class="copy">© 2013 Company Name.&nbsp; All right reserved.&nbsp; Term of Use</div>
  <svg width="140" height="34" aria-label="Social links">
    <circle cx="17" cy="17" r="16" fill="#111"/>
    <circle cx="52" cy="17" r="16" fill="#111"/>
    <circle cx="87" cy="17" r="16" fill="#111"/>
    <circle cx="122" cy="17" r="16" fill="#111"/>
  </svg>
</footer>
</body>
</html>
```